High-end Oceanfront Real Estate Group Needs Clean, Modern Web Design

I’m looking for a clean, professional, modern and beautiful homepage web design for a Real Estate group in Southern California, USA.

The group/company is “Marlow on the Shore,” and they specialize in high end (i.e. expensive), oceanfront real estate in the Orange County area.

The look and feel of the page should accentuate the brand qualities: luxurious/expensive, professional, and beautiful (Orange County is one of the most beautiful areas in all the US and we would love the site to emphasize the beautiful beaches and scenery it has to offer).

Looks we like:
• www.brantleyhomesrealty.example
• www.keptbyfenwick.example -- I think the design is pretty out-dated in this site, but I like the organization/layout of the site

Header Tags (I don’t know if we can fit all of these, may need a side-menu, but I’d prefer header title only if possible):
• Welcome
• Featured Listings
• Previously Sold
• Sell
• Property Search
• Team
• Videos
• Blog
• Explore O.C.
• Contact

I have attached the beach and logo pics that we would like to use as the header, a few pictures of the team, and one sample home/view pic which can be used in any of the other sections (for pictures of the homes, just find expensive oceanfront houses and that will be fine).

I promise to provide feedback to each and every design submission. I appreciate the hard work that all of you are putting into your designs. There can be only one contest winner, but I hope to give all of you helpful feedback to submit the best designs possible!

Target Market(s)

Very wealthy home owners of oceanfront properties. These properties are worth several millions of dollars, and thus the site and brand needs to be targeted to very wealthy, successful individuals and families (both US and international buyers).

Industry/Entity Type

Real Estate

Number of Pages Required

2 page

Requirements
Must have
• I don’t want to give too many requirements, because I want to let you all be creative. However, here are the few Must Haves:
• Must submit 2 page designs (a home page and a sub page)
• Must use logo provided
• Focus is mostly on homes, but I would like to include some beach/ocean imagery as well
• The first “item” on the home page should be an accordion/slider which shows pictures of homes and with 1 line of text: “List with the Leader” and two link buttons: “Sell Your Home” and “Buy Your Home”
• Color palette needs to be mainly blues--to match ocean and sky blue
• Exported in all major formats (psd,ai,eps,png,jpeg,etc)
Nice to have
• We don’t necessarily need all of these, but would like to feature most:
• List of videos
• “Meet the Team”—brief team bios and pics
• Link(s) to Blog
• “List with the Leader” – section on why they should choose this firm
• Featured Listings
• Previously Sold

```html
<!DOCTYPE html>
<html lang="en">
<head>
<meta charset="utf-8">
<title>Marlow on the Shore — Oceanfront Real Estate</title>
<link href="https://fonts.googleapis.com/css2?family=Roboto:wght@300;400;500;700&display=swap" rel="stylesheet">
<style>
:root{
  --blue:#1b8fd2;
  --orange:#f47b20;
  --orange-deep:#e2661a;
  --brown:#3b2b23;
  --ink:#333333;
  --muted:#666666;
  --mist:#eef0f2;
  --white:#ffffff;
}
*{box-sizing:border-box;margin:0;padding:0}
html,body{width:1200px;height:4986px;overflow:hidden}
body{font-family:"Roboto",Arial,sans-serif;color:var(--ink);background:var(--white);position:relative}
section,header,footer{position:absolute;left:0;width:1200px}
.abs{position:absolute}
.ph{position:absolute}
.pill{position:absolute;display:flex;align-items:center;justify-content:center;border-radius:22px;font-size:14px;font-weight:500;letter-spacing:.5px;text-transform:uppercase}
.section-title{position:absolute;left:0;width:1200px;text-align:center;font-weight:300;font-size:40px;letter-spacing:3px;text-transform:uppercase;color:#444}
.section-sub{position:absolute;left:0;width:1200px;text-align:center;font-size:15px;color:var(--muted)}
.arrow{position:absolute;display:flex;align-items:center;justify-content:center;color:#fff;font-size:26px}

/* header */
.site-header{top:0;height:133px;background:rgba(255,255,255,.9);z-index:2}
.brand{left:130px;top:22px;width:200px;font-size:40px;line-height:40px;font-weight:300;color:#555;text-transform:uppercase;letter-spacing:1px}
.brand small{display:block;font-size:16px;line-height:18px;letter-spacing:4px}
.top-bar{right:110px;top:26px;display:flex;align-items:center;gap:18px;font-size:12px;color:#555}
.top-bar .phone{font-size:22px;color:#333}
.top-bar .search{width:150px;border-bottom:1px solid #aaa;color:#999;padding-bottom:2px}
.top-bar .social{display:flex;gap:12px}
.top-bar .social i{display:block;width:16px;height:16px;background:#555;border-radius:3px}
.main-nav{left:415px;top:76px;display:flex;gap:30px;font-size:16px;font-weight:500;text-transform:uppercase;color:#444;align-items:center}
.main-nav .active{background:var(--blue);color:#fff;padding:8px 20px;border-radius:20px}

/* hero */
.hero{top:0;height:698px;background:linear-gradient(180deg,#9fb5c8 0%,#6f8c6c 30%,#c9c3b4 55%,#6d8ea0 75%,#b7ad9a 100%)}
.hero h1{position:absolute;top:330px;width:1200px;text-align:center;font-weight:300;font-size:58px;letter-spacing:5px;color:#fff}
.hero .sell{left:450px;top:434px;width:140px;height:42px;color:#fff;border:1px solid rgba(255,255,255,.7);background:rgba(0,0,0,.15)}
.hero .buy{left:625px;top:434px;width:150px;height:42px;color:#fff;background:var(--orange)}

/* welcome */
.welcome{top:698px;height:316px;background:var(--mist)}
.welcome .section-title{top:52px}
.welcome p{position:absolute;left:165px;width:870px;top:128px;text-align:center;font-size:15px;line-height:24px;color:var(--muted)}
.welcome .more{left:515px;top:215px;width:170px;height:40px;background:var(--blue);color:#fff}

/* featured */
.featured{top:1014px;height:675px}
.featured .section-title{top:50px}
.featured .section-sub{top:110px}
.grid{position:absolute;top:183px;left:0;width:1200px;height:492px;display:grid;grid-template-columns:repeat(4,300px);grid-template-rows:repeat(2,246px)}
.listing-feature{background:var(--orange);color:#fff;text-align:center;padding-top:38px}
.listing-feature b{display:block;font-size:44px;font-weight:400}
.listing-feature h3{font-size:22px;font-weight:400;text-transform:uppercase;letter-spacing:1px}
.listing-feature p{font-size:13px;line-height:18px;margin:8px 40px}
.listing-feature span{font-size:13px}

/* sell */
.sell-block{top:1689px;height:438px}
.sell-block h2{position:absolute;left:110px;top:66px;font-size:38px;font-weight:300;letter-spacing:2px;color:#444}
.sell-block .lead{position:absolute;left:110px;top:120px;width:280px;font-size:14px;line-height:21px;color:var(--muted)}
.sell-block .more{left:110px;top:198px;width:125px;height:38px;background:#333;color:#fff;font-size:12px}
.feature{position:absolute;width:300px}
.feature svg{position:absolute;left:0;top:0}
.feature h4{margin-left:53px;font-size:15px;font-weight:500;color:#333}
.feature p{margin-left:53px;font-size:12px;line-height:17px;color:var(--muted);margin-top:4px}

/* property search */
.search-block{top:2127px;height:532px;background:linear-gradient(180deg,#e46b1c 0%,#f08a3a 40%,#f27a22 100%)}
.search-block .section-title{top:70px;color:#fff}
.search-block .section-sub{top:132px;color:#fff}
.carousel{position:absolute;top:193px;left:0;width:1200px;height:240px}
.carousel .card{position:absolute;top:0;width:220px;height:240px;background:#fff;padding:34px 24px;font-size:13px;line-height:18px;color:var(--muted)}
.carousel .card h3{font-size:18px;font-weight:400;color:#333;margin-bottom:8px}
.carousel .card .more{position:relative;width:110px;height:30px;margin-top:14px;background:#333;color:#fff;font-size:11px}
.searchbar{position:absolute;left:372px;top:466px;width:460px;height:40px;background:#fff;display:flex;align-items:center;padding:0 0 0 18px;font-size:13px;color:#bbb}
.searchbar .btn{position:absolute;right:6px;top:6px;width:100px;height:28px;background:var(--orange);color:#fff;display:flex;align-items:center;justify-content:center;font-size:14px}

/* team */
.team{top:2692px;height:516px;background:var(--brown);color:#eee}
.team h2{position:absolute;left:540px;top:100px;font-size:40px;font-weight:300;letter-spacing:3px}
.team .role{position:absolute;left:540px;top:160px;font-size:15px}
.team .bio{position:absolute;left:540px;width:560px;font-size:14px;line-height:22px;color:#ddd}
.team .more{left:540px;top:388px;width:120px;height:38px;background:#fff;color:#333;font-size:12px}
.team .arrow{width:32px;height:90px;border:1px solid #999;top:220px;font-size:22px}

/* video */
.video-intro{top:3208px;height:189px}
.video-intro .section-title{top:50px}
.video-intro p{position:absolute;left:320px;width:560px;top:122px;text-align:center;font-size:14px;line-height:22px;color:var(--muted)}
.video-intro a{color:var(--blue);text-decoration:underline}
.video-band{top:3397px;height:525px;background:linear-gradient(180deg,#1d2b3f 0%,#344a63 45%,#6a5a3e 70%,#1b2535 100%)}
.video-band h2{position:absolute;top:295px;width:1200px;text-align:center;font-size:46px;font-weight:700;color:#fff;letter-spacing:1px}

/* blog */
.blog{top:3922px;height:492px}
.blog h2{position:absolute;left:143px;top:100px;font-size:40px;font-weight:300;color:var(--blue);letter-spacing:2px}
.blog .meta{position:absolute;left:143px;top:166px;font-size:15px;color:#444}
.blog .meta span{color:var(--blue)}
.blog .body{position:absolute;left:143px;width:600px;font-size:14px;line-height:21px;color:var(--muted)}
.blog .more{left:143px;top:372px;width:120px;height:38px;background:var(--blue);color:#fff;font-size:12px}
.blog .arrow{top:205px;width:30px;height:90px}

/* map */
.map{top:4414px;height:422px;background:linear-gradient(120deg,#dfe3d3 0%,#e9e6da 45%,#cfd9c1 75%,#b7c99f 100%)}
.map-card{position:absolute;left:392px;top:117px;width:339px;height:249px;background:#fff;box-shadow:0 2px 8px rgba(0,0,0,.25)}
.map-card .photo{position:absolute;left:0;top:0;width:339px;height:110px;background:linear-gradient(180deg,#7d8fa2,#9c8868)}
.map-card .name{position:absolute;left:20px;top:124px;width:140px;font-size:16px;line-height:20px;font-weight:500;color:#555;text-transform:uppercase}
.map-card .line{position:absolute;left:120px;font-size:13px;color:#444;display:flex;align-items:center;gap:8px}

/* footer */
.site-footer{top:4836px;height:150px}
.social-row{position:absolute;left:455px;top:38px;display:flex;gap:14px}
.social-row i{display:block;width:48px;height:48px;border-radius:6px;background:#4f6fa5}
.site-footer p{position:absolute;top:102px;width:1200px;text-align:center;font-size:13px;color:#444}
</style>
</head>
<body>

<section class="hero" role="img" aria-label="Photograph of a luxury estate terrace with balustrades and a fountain overlooking the coast">
  <h1>List with the Leader</h1>
  <div class="pill sell">Sell Your Home</div>
  <div class="pill buy">Buy Your Home</div>
</section>

<header class="site-header">
  <div class="abs brand">Marlow<small>on the shore</small></div>
  <div class="abs top-bar">
    <span>CALL US TODAY</span>
    <svg width="20" height="20" viewBox="0 0 24 24"><path d="M6.6 10.8a15 15 0 0 0 6.6 6.6l2.2-2.2a1 1 0 0 1 1-.25 11.4 11.4 0 0 0 3.6.6 1 1 0 0 1 1 1V20a1 1 0 0 1-1 1A17 17 0 0 1 3 4a1 1 0 0 1 1-1h3.5a1 1 0 0 1 1 1c0 1.25.2 2.45.6 3.6a1 1 0 0 1-.25 1z" fill="#333"/></svg>
    <span class="phone">949-555-0142</span>
    <span class="search">Search</span>
    <svg width="16" height="16" viewBox="0 0 16 16"><circle cx="6.5" cy="6.5" r="5" fill="none" stroke="#555" stroke-width="2"/><path d="M10.5 10.5 15 15" stroke="#555" stroke-width="2"/></svg>
    <span class="social"><i></i><i></i><i></i><i></i></span>
  </div>
  <nav class="abs main-nav">
    <span class="active">Home</span><span>Sell</span><span>Property Search</span><span>Team</span><span>Videos</span><span>Blog</span><span>Contact</span>
  </nav>
</header>

<section class="welcome">
  <h2 class="section-title">Welcome Marlow on the Shore</h2>
  <p>We at MarlowontheShore are privileged to help people from all over the world find their dream homes in Monarch Beach, Laguna Beach, Newport Coast, Dana Point, San Clemente and San Juan Capistrano. Whether you are buying or selling a property in Orange County, we want to help you in the most efficient, professional way possible.</p>
  <div class="pill more">Read More</div>
</section>

<section class="featured">
  <h2 class="section-title">Featured Listings</h2>
  <p class="section-sub">Lorem Ipsum is simply dummy text of the printing industry. Lorem Ipsum standard dummy text.</p>
  <div class="grid">
    <div role="img" aria-label="Photograph of a coastal home at dusk" style="background:linear-gradient(160deg,#3f7fb5,#c98a4a)"></div>
    <div role="img" aria-label="Photograph of a lit modern villa at night" style="background:linear-gradient(160deg,#2b3447,#c0894f)"></div>
    <div class="listing-feature"><b>42</b><h3>Coral Vista Drive</h3><p>Lorem Ipsum is simply dummy text of the printing industry. Lorem Ipsum and</p><span>Dana point | Active</span></div>
    <div role="img" aria-label="Photograph of a Mediterranean house with a pool" style="background:linear-gradient(160deg,#7fa7d4,#c9a27c)"></div>
    <div role="img" aria-label="Photograph of a villa with an evening pool" style="background:linear-gradient(160deg,#24354f,#3c8fb8)"></div>
    <div role="img" aria-label="Photograph of a large estate lit at twilight" style="background:linear-gradient(160deg,#2a3a5a,#b07a45)"></div>
    <div role="img" aria-label="Photograph of a modern home with an illuminated pool" style="background:linear-gradient(160deg,#1e2d4c,#2c86c4)"></div>
    <div role="img" aria-label="Photograph of a stucco house under a blue sky" style="background:linear-gradient(160deg,#7ba4cf,#9a6f52)"></div>
  </div>
  <div class="arrow" style="left:0;top:408px;width:22px;height:60px;background:var(--blue)">‹</div>
  <div class="arrow" style="right:0;top:408px;width:22px;height:60px;background:var(--orange)">›</div>
</section>

<section class="sell-block">
  <h2>SELL</h2>
  <p class="lead">Lorem Ipsum is simply dummy text of the printing industry. Lorem Ipsum standard dummy text.</p>
  <div class="pill more">Read More</div>

  <div class="feature" style="left:455px;top:68px">
    <svg width="34" height="34" viewBox="0 0 34 34"><circle cx="17" cy="17" r="14" fill="none" stroke="#333" stroke-width="2.5"/></svg>
    <h4>Lorem Ipsum dummy</h4><p>Lorem Ipsum is simply dummy text of the printing industry Lorem Ipsum.</p>
  </div>
  <div class="feature" style="left:820px;top:68px">
    <svg width="40" height="34" viewBox="0 0 40 34"><ellipse cx="20" cy="17" rx="18" ry="10" fill="none" stroke="#333" stroke-width="2.5"/><circle cx="20" cy="17" r="5" fill="#333"/></svg>
    <h4>Lorem Ipsum dummy</h4><p>Lorem Ipsum is simply dummy text of the printing industry Lorem Ipsum.</p>
  </div>
  <div class="feature" style="left:455px;top:191px">
    <svg width="38" height="34" viewBox="0 0 38 34"><rect x="6" y="7" width="26" height="17" fill="none" stroke="#333" stroke-width="2.5"/><path d="M2 28h34" stroke="#333" stroke-width="3"/></svg>
    <h4>Lorem Ipsum dummy</h4><p>Lorem Ipsum is simply dummy text of the printing industry Lorem Ipsum.</p>
  </div>
  <div class="feature" style="left:820px;top:191px">
    <svg width="34" height="34" viewBox="0 0 34 34"><rect x="3" y="14" width="7" height="16" fill="#333"/><path d="M12 14l6-10c3 0 4 2 3 6h9c2 0 3 2 2 4l-3 14H12z" fill="#333"/></svg>
    <h4>Lorem Ipsum dummy</h4><p>Lorem Ipsum is simply dummy text of the printing industry Lorem Ipsum.</p>
  </div>
  <div class="feature" style="left:455px;top:314px">
    <svg width="34" height="34" viewBox="0 0 34 34"><path d="M17 30 4 17a7 7 0 0 1 13-9 7 7 0 0 1 13 9z" fill="none" stroke="#333" stroke-width="2.5"/></svg>
    <h4>Lorem Ipsum dummy</h4><p>Lorem Ipsum is simply dummy text of the printing industry Lorem Ipsum.</p>
  </div>
  <div class="feature" style="left:820px;top:314px">
    <svg width="36" height="34" viewBox="0 0 36 34"><path d="M3 26a15 15 0 0 1 30 0z" fill="#333"/><circle cx="18" cy="26" r="3" fill="#fff"/></svg>
    <h4>Lorem Ipsum dummy</h4><p>Lorem Ipsum is simply dummy text of the printing industry Lorem Ipsum.</p>
  </div>
</section>

<section class="search-block">
  <h2 class="section-title">Property Search</h2>
  <p class="section-sub">Lorem Ipsum is simply dummy text of the printing industry. Lorem Ipsum standard dummy text.</p>
  <div class="carousel">
    <div class="ph" role="img" aria-label="Photograph of a pier at sunset" style="left:0;top:0;width:200px;height:240px;background:linear-gradient(180deg,#3b4f86,#d98a52)"></div>
    <div class="ph" role="img" aria-label="Photograph of a hillside estate" style="left:223px;top:0;width:202px;height:240px;background:linear-gradient(180deg,#8fb1d6,#7d6a4c)"></div>
    <div class="ph" role="img" aria-label="Photograph of a warmly lit interior" style="left:448px;top:0;width:200px;height:240px;background:linear-gradient(180deg,#7a4a2a,#c98a4a)"></div>
    <div class="card" style="left:655px"><h3>LOREM IPSUM</h3>Lorem Ipsum is simply dummy text of the printing industry. Lorem Ipsum standard dummy text.<div class="pill more">Read More</div></div>
    <div class="ph" role="img" aria-label="Photograph of a white arched courtyard" style="left:903px;top:0;width:202px;height:240px;background:linear-gradient(180deg,#c9d2c8,#6f8a5c)"></div>
    <div class="ph" role="img" aria-label="Photograph of a coastal home" style="left:1128px;top:0;width:72px;height:240px;background:linear-gradient(180deg,#6f98c4,#a87f5a)"></div>
    <div class="arrow" style="left:0;top:90px;width:22px;height:60px;background:var(--blue)">‹</div>
    <div class="arrow" style="right:0;top:90px;width:22px;height:60px;background:var(--orange)">›</div>
  </div>
  <div class="searchbar">Lorem Ipsum is simply<span class="btn">Search</span></div>
</section>

<section class="team">
  <div class="ph" role="img" aria-label="Portrait photograph of the lead agent in a grey suit" style="left:115px;top:33px;width:335px;height:483px;background:linear-gradient(180deg,#5a4a3f,#7d8089 60%,#4e5563)"></div>
  <h2>TEAM</h2>
  <p class="role">Lorem Ipsum is simply dummy text.</p>
  <p class="bio" style="top:210px">Lorem Ipsum is simply dummy text of the printing industry. Lorem Ipsum standard dummy text. Lorem Ipsum is simply dummy text of the printing industry. Lorem Ipsum standard dummy text. Lorem Ipsum is simply dummy text of the printing industry. Lorem Ipsum standard dummy text.</p>
  <p class="bio" style="top:310px">Lorem Ipsum is simply dummy text of the printing industry. Lorem Ipsum standard dummy text. Lorem Ipsum is simply dummy text.</p>
  <div class="pill more">Read More</div>
  <div class="arrow" style="left:40px">‹</div>
  <div class="arrow" style="left:1128px">›</div>
</section>

<section class="video-intro">
  <h2 class="section-title">Our Video</h2>
  <p>Lorem Ipsum is simply dummy text of the printing industry. Lorem Ipsum standard Lorem Ipsum standard dummy text. <a>Read More</a></p>
</section>

<section class="video-band" role="img" aria-label="Night aerial photograph of a lit harbour and city">
  <svg class="abs" style="left:552px;top:185px" width="96" height="96" viewBox="0 0 96 96"><circle cx="48" cy="48" r="46" fill="#fff"/><path d="M38 28v40l32-20z" fill="#333"/></svg>
  <h2>WATCH INTRO VIDEO</h2>
</section>

<section class="blog">
  <h2>BLOG</h2>
  <p class="meta">Post by : <span>avery.lane</span> / 03 / march / 2015</p>
  <p class="body" style="top:196px">Lorem Ipsum is simply dummy text of the printing industry. Lorem Ipsum standard dummy text. Lorem Ipsum is simply dummy text of the printing industry. Lorem Ipsum standard dummy text. Lorem Ipsum is simply dummy text of the printing industry. Lorem Ipsum standard dummy text.</p>
  <p class="body" style="top:290px">Lorem Ipsum is simply dummy text of the printing industry. Lorem Ipsum standard dummy text. Lorem Ipsum is simply dummy text.</p>
  <div class="pill more">Read More</div>
  <div class="ph" role="img" aria-label="Portrait photograph of a team member in a light blazer" style="left:791px;top:60px;width:266px;height:373px;background:linear-gradient(180deg,#a8c4d8,#d9c2ad 55%,#b59b86)"></div>
  <div class="arrow" style="left:55px;background:var(--blue)">‹</div>
  <div class="arrow" style="left:1115px;background:var(--orange)">›</div>
</section>

<section class="map" role="img" aria-label="Road map of Southern California around the office">
  <svg class="abs" style="left:745px;top:95px" width="22" height="32" viewBox="0 0 22 32"><path d="M11 31S2 18 2 11a9 9 0 0 1 18 0c0 7-9 20-9 20z" fill="#e0362c"/><circle cx="11" cy="11" r="3.5" fill="#fff"/></svg>
  <div class="map-card">
    <div class="photo" role="img" aria-label="Photograph of the office building"></div>
    <div class="name">Marlow<br>on the Shore</div>
    <div class="line" style="top:180px"><svg width="12" height="16" viewBox="0 0 12 16"><path d="M6 15S1 9 1 5.5a5 5 0 0 1 10 0C11 9 6 15 6 15z" fill="#555"/></svg>12 Harbor Row, Southern California, USA</div>
    <div class="line" style="top:208px"><svg width="14" height="14" viewBox="0 0 24 24"><path d="M6.6 10.8a15 15 0 0 0 6.6 6.6l2.2-2.2a1 1 0 0 1 1-.25 11.4 11.4 0 0 0 3.6.6 1 1 0 0 1 1 1V20a1 1 0 0 1-1 1A17 17 0 0 1 3 4a1 1 0 0 1 1-1h3.5a1 1 0 0 1 1 1c0 1.25.2 2.45.6 3.6a1 1 0 0 1-.25 1z" fill="#555"/></svg>949-555-0142</div>
  </div>
</section>

<footer class="site-footer">
  <div class="social-row"><i></i><i style="background:#c8343a"></i><i style="background:#3ba7e4"></i><i style="background:#3d6fb5"></i><i style="background:#6d5a4a"></i></div>
  <p>Copyright © 2015 - Marlow on the Shore.com</p>
</footer>

</body>
</html>
```